Grins Circle Brochure highlighting office, club membership, dentist to attract new members

This brochure is for prospective patients who are interested in joining our Exclusive Member Only program. The brochure should explain the exclusivity of the club, club fees, membership benefits, office hightlights, friendly staff, experienced Dentist, Also can refer to our website www.dentistvorlani.example for more information to go into brochure.

Our mission is to provide a quality care your smile needs, comfort & luxury you deserve.

Staff - Our dedicated, friendly & experience staff are well equipped to answer all your questions and make every visit as memorable as the previous the one. We believe Care for your comfort is as important as Care your Smile needs. We strive to make every aspect of your visit as smooth and effortless as possible.

Dentist - Dr. Vorlani, I have extensive experience in general, cosmetic & orthodontic treatments. I continue to attend continued education more than required by the dental association. My only motivation is to bring the best of the procedures and technology available in the market today for my patients. I am also a member of many professional organizations in DC metro area which helps share and promote best practices in the industry. Outside of Dentistry I love to spend time with my 6 and 2 yr olds as a nature lover I get to hike regularly, as weather gets cold, I love to hit the thread mil with my fav music. Yoga stretches are part of my in between procedures.

Office - Our office has been in the current location for over 30 years. Our office has been updated continuously, however we continue to keep the warm and relaxing ambience. The reception area is the hallmark of our core principle. The coffee station with the traditional seating helps us set the warm and cozy tone for the rest of the office. The water fountain adds the relaxing experience. Though many patients have noted they don’t get to enjoy the reception area as they don’t usually get to wait. We take that as a compliment.

Operatory
We have three operatories Harmony, Tranquility & Serenity each named to reflect the essence we strive for in all aspect of our practice. Each operatory is equipped with varied tempurpedic firmness for your comfort. All the operatories are kept clean and well organized for visual and functional smoothness. The technologies are kept upto date to ensure our services are unparalleled. We offer warm cotton towels during long procedures to ensure comfortness. We make individual eye shades to protect the eyes.

Restroom
Last but not the least we are proud of our restroom, we ensure our standards and attention to the details are carried through and through. Cotton towels are available to help freshen up after a long procedure.

The Club
I know you have been waiting to know about the club. I saved the best to the last. Grins Circle is the crown jewel of our practice. As part of my quest to continue to improve our services, after a considerable thought and iterations we conceived this program. The core objective is to bring another level of comfort to our patients. The program brings all the aspects of our being together in a simple package. Instead of breaking the essentials like cleaning, Xrays, Fluoride, whitening, diagnosis, consultation,emergency visits,, we simplified everything into one simple club membership. As a member of Grins Circle you will get all of the basic essentials included in your program. Also you will receive membership discounts from 15% to 25% in all the procedures. The best part of the program is all your procedures cost can be financed at 0% interest. As always our staff stay on top of your essential treatments, reaching out to you by your preferred mode of contact and ensure you get your essentials done at your convenience.

Pricing

The Grins Circle program is a subscription program. Patients pay monthly subscription. This simple monthly subscription covers all the essential routine dental care including Cleaning, XRays, Fluoride treatment, Whitening, Diagnosis, Consultation, Emergency visits.

Single membership is $59 a month
Family of Two membership is $49 per person per month
Family of Three and more is $39 per person per month

Members receive 15% to 25% discounts on all of the below procedures

Orthodontic - Clearvanta, Braces
Implants
Bridges
Crowns
Tooth Extractions
Relaxyn treatments
Laser Gum Treatments
Veneers, Bonding
Fillings
Dentures

Target Market(s)

high income group, family, professionals, teens

Industry/Entity Type

Club

Font styles to use
Script

Colors
3176b5

Requirements
Must have
• Logo, pic of Dentist, office pics

```html
<!DOCTYPE html>
<html lang="en">
<head>
<meta charset="utf-8">
<title>Grins Circle Brochure</title>
<link rel="stylesheet" href="https://fonts.googleapis.com/css2?family=Great+Vibes&family=Roboto:wght@400;700&family=Roboto+Condensed:wght@400;700&display=swap">
<style>
  :root {
    --brand-blue: #3176b5;
    --ink-black: #000000;
    --page-grey: #3b3b3c;
    --paper: #ffffff;
    --text-dark: #1a1a1a;
    --rule-grey: #9a9a9a;
  }
  * { box-sizing: border-box; margin: 0; padding: 0; }
  html, body { width: 832px; height: 1200px; overflow: hidden; }
  body { background: var(--page-grey); position: relative; font-family: "Roboto", Arial, sans-serif; }

  .brochure {
    position: absolute; left: 47px; top: 78px; width: 738px; height: 1044px;
    background: var(--ink-black); overflow: hidden;
  }

  .masthead { position: absolute; left: 0; top: 0; width: 738px; height: 220px; }
  .masthead svg { position: absolute; left: 0; top: 0; }
  .masthead-title {
    position: absolute; left: 0; top: 4px; width: 100%; text-align: center;
    font-family: "Great Vibes", cursive; font-size: 84px; color: var(--paper);
    letter-spacing: 1px; line-height: 1.2;
  }

  .staff-intro {
    position: absolute; left: 22px; top: 146px; width: 696px;
    font-family: "Roboto Condensed", Arial, sans-serif; font-size: 14.6px; line-height: 20px;
    color: var(--paper);
  }
  .section-label {
    font-family: "Roboto Condensed", Arial, sans-serif; font-weight: 700;
    color: var(--brand-blue); font-size: 19px;
  }

  .blue-rule { position: absolute; left: 0; top: 218px; width: 738px; height: 3px; background: var(--brand-blue); }

  .team-photo {
    position: absolute; left: 0; top: 222px; width: 738px; height: 209px;
    background: linear-gradient(90deg, #5b4a3e 0%, #3f8fa8 22%, #6a4636 34%, #4aa1bb 50%, #7a5a48 66%, #3d93ad 80%, #c9d4dc 100%);
  }

  .dentist-bio {
    position: absolute; left: 0; top: 431px; width: 738px; height: 151px;
    background: var(--paper); padding: 6px 22px 0 22px;
    font-family: "Roboto Condensed", Arial, sans-serif; font-size: 13.6px; line-height: 19.6px;
    color: var(--text-dark); text-align: justify;
  }

  .club-feature {
    position: absolute; left: 0; top: 582px; width: 738px; height: 253px;
    background: var(--ink-black); padding: 0 22px;
  }
  .club-heading {
    text-align: center; font-family: "Roboto Condensed", Arial, sans-serif; font-weight: 700;
    color: var(--brand-blue); font-size: 43px; line-height: 50px; margin-top: 17px;
  }
  .club-text {
    font-family: "Roboto Condensed", Arial, sans-serif; color: var(--paper);
    font-size: 23px; line-height: 35px; text-align: justify; margin-top: 1px;
  }

  .contact-panel {
    position: absolute; left: 0; top: 835px; width: 738px; height: 209px; background: var(--paper);
  }
  .location { position: absolute; top: 27px; font-family: "Roboto", Arial, sans-serif; font-size: 14.2px; line-height: 19.6px; color: var(--text-dark); }
  .location-north { left: 22px; }
  .location-west { left: 245px; }
  .location-name { color: var(--brand-blue); font-weight: 700; font-family: "Roboto Condensed", Arial, sans-serif; font-size: 15px; }
  .location-phone { margin-top: 4px; }
  .location-phone strong { color: var(--brand-blue); font-size: 19px; font-family: "Roboto Condensed", Arial, sans-serif; }
  .website {
    position: absolute; left: 22px; top: 150px; font-family: "Roboto", Arial, sans-serif;
    font-weight: 700; font-size: 34px; color: var(--brand-blue); letter-spacing: -0.3px;
  }
  .area-map {
    position: absolute; left: 482px; top: 6px; width: 243px; height: 180px; border-radius: 50%;
    background: radial-gradient(ellipse at 50% 45%, #eef1e8 0%, #dfe8d2 60%, #c9d8bd 100%);
    border: 3px solid #e6e6e6; box-shadow: 0 3px 6px rgba(0,0,0,0.35);
  }
</style>
</head>
<body>
  <main class="brochure">
    <header class="masthead">
      <svg width="738" height="220" viewBox="0 0 738 220" aria-hidden="true">
        <path d="M0 0 H738 V80 Q369 180 0 80 Z" fill="#3176b5"/>
        <path d="M0 82 Q369 182 738 82" fill="none" stroke="#9a9a9a" stroke-width="3"/>
      </svg>
      <h1 class="masthead-title">Grins Circle</h1>
    </header>

    <p class="staff-intro"><span class="section-label">Staff</span> - Our dedicated, friendly &amp; experience staff are well equipped to answer all your questions and make every visit as memorable as the previous the one. We believe Care for your comfort is as important as Care your needs. We strive to make every aspect of your visit as smooth and effortless as possible.</p>

    <div class="blue-rule"></div>
    <div class="team-photo" role="img" aria-label="Team photo of the dentist and four staff members in teal scrubs in the office"></div>

    <section class="dentist-bio">
      <p><span class="section-label">Dentist</span> - Dr. Vorlani, I have extensive experience in general, cosmetic &amp; orthodontic treatments. I continue to attend continued education more than required by the dental association. My only motivation is to bring the best of the procedures and technology available in the market today for my patients. I am also a member of many professional organizations in DC metro area which helps share and promote best practices in the industry. Outside of Dentistry I love to spend time with my 6 and 2 yr olds as a nature lover I get to hike regularly, as weather gets cold, I love to hit the thread mil with my fav music. Yoga stretches are part of my in between procedures.</p>
    </section>

    <section class="club-feature">
      <h2 class="club-heading">The Club</h2>
      <p class="club-text">I know you have been waiting to know about the club. I saved the best to the last. Grins Circle is the crown jewel of our practice. As part of my quest to continue to improve our services, after a considerable thought and iterations we conceived this program. The core objective is to bring another level of comfort to our patients.</p>
    </section>

    <footer class="contact-panel">
      <div class="location location-north">
        <div class="location-name">Grins of Larkmoor</div>
        <div>4820 Hollin Ave, Suite 114</div>
        <div>Brenton, MD, United States</div>
        <div>20990</div>
        <div class="location-phone">Call us @ <strong>301-555-0147</strong></div>
      </div>
      <div class="location location-west">
        <div class="location-name">Grins of Westvale</div>
        <div>6310 Fernway Rd, Suite 212</div>
        <div>Westvale, MD, United States</div>
        <div>20995</div>
        <div class="location-phone">Call us @ <strong>301-555-0182</strong></div>
      </div>
      <div class="website">www.dentistvorlani.example</div>
      <div class="area-map" role="img" aria-label="Oval area map showing the office location marked with a blue arrow"></div>
    </footer>
  </main>
</body>
</html>
```